Copper & Wren Labels*

Hello :) I am needing labels for my herbal tea/petal product. I am a small producer for the local restaurants (edible flowers/micro herbs & dried product). I am hoping to sell the dried product online. It will be sold in batches as it is ready so quite small/boutique and the label needs to be somewhat generic for the range of produce I make.
Feels: no/minimal plastic, product is in a reusable mason jar, we use organic/regenerative principles from soil health to end product. Treading gently on the land. High quality i.e only fresh hand picked leaf tips for the tea.

```html
<!DOCTYPE html>
<html lang="en">
<head>
<meta charset="UTF-8">
<title>Copper &amp; Wren – Single Origin Herbal Tea Label</title>
<link href="https://fonts.googleapis.com/css2?family=Great+Vibes&family=Josefin+Sans:wght@300;400&family=Quicksand:wght@700&display=swap" rel="stylesheet">
<style>
  :root {
    --sage: #5f8265;
    --sage-pale: #cfe0d1;
    --paper: #ffffff;
  }
  html, body {
    margin: 0;
    padding: 0;
    background: var(--paper);
    overflow: hidden;
  }
  .label {
    position: relative;
    width: 1017px;
    height: 1200px;
    background: var(--paper);
    overflow: hidden;
    color: var(--sage);
    font-family: "Josefin Sans", sans-serif;
    font-weight: 300;
  }
  .label__frame {
    position: absolute;
    left: 80px;
    top: 78px;
    width: 857px;
    height: 1046px;
    border: 4px solid var(--sage);
  }
  .brand {
    position: absolute;
    left: 280px;
    top: 116px;
    display: flex;
    align-items: center;
    gap: 26px;
  }
  .brand__dot {
    width: 104px;
    height: 104px;
    border-radius: 50%;
    background: var(--sage);
  }
  .brand__name {
    font-family: "Quicksand", sans-serif;
    font-weight: 700;
    font-size: 42px;
    letter-spacing: 1px;
    color: var(--sage);
  }
  .title {
    position: absolute;
    left: 80px;
    width: 865px;
    margin: 0;
    text-align: center;
  }
  .title__kicker {
    top: 280px;
    font-size: 31px;
    letter-spacing: 3px;
    text-transform: uppercase;
    font-weight: 400;
  }
  .title__main {
    top: 312px;
    font-family: "Great Vibes", cursive;
    font-weight: 400;
    font-size: 96px;
    line-height: 1.2;
  }
  .field-tag {
    position: absolute;
    left: 105px;
    width: 215px;
    height: 60px;
    background: var(--sage);
    color: var(--paper);
    font-size: 23px;
    letter-spacing: 2px;
    text-transform: uppercase;
    box-sizing: border-box;
    padding: 22px 0 0 21px;
  }
  .field-tag--leaf { top: 497px; }
  .field-tag--petals { top: 690px; }
  .field-tag--batch { top: 835px; }
  .options {
    position: absolute;
    left: 400px;
    top: 492px;
    margin: 0;
    padding: 0;
    list-style: none;
  }
  .options__item {
    display: flex;
    align-items: center;
    height: 60px;
    font-size: 25px;
    letter-spacing: 2px;
    text-transform: uppercase;
  }
  .options__box {
    width: 20px;
    height: 20px;
    border: 3px solid var(--sage);
    border-radius: 50%;
    margin-right: 16px;
    margin-bottom: 6px;
  }
  .rule {
    position: absolute;
    left: 105px;
    width: 816px;
    height: 3px;
    background: var(--sage);
  }
  .rule--one { top: 672px; }
  .rule--two { top: 814px; }
  .flower-art {
    position: absolute;
    left: 606px;
    top: 884px;
    width: 246px;
    height: 210px;
    background: radial-gradient(ellipse at 55% 45%, var(--sage-pale) 0%, rgba(207,224,209,0.45) 55%, rgba(255,255,255,0) 72%);
  }
  .origin {
    position: absolute;
    left: 126px;
    top: 1003px;
    font-size: 26px;
    letter-spacing: 2.5px;
    text-transform: uppercase;
    line-height: 54px;
    font-weight: 300;
  }
  .origin p { margin: 0; }
</style>
</head>
<body>
  <main class="label">
    <div class="label__frame"></div>

    <header class="brand">
      <div class="brand__dot"></div>
      <span class="brand__name">Copper &amp; Wren</span>
    </header>

    <div class="title title__kicker">Single Origin</div>
    <h1 class="title title__main">Herbal Tea</h1>

    <div class="field-tag field-tag--leaf">Leaf Base:</div>
    <ul class="options">
      <li class="options__item"><span class="options__box"></span>Lemon Verbena</li>
      <li class="options__item"><span class="options__box"></span>Mint</li>
      <li class="options__item"><span class="options__box"></span>Agastache</li>
    </ul>
    <div class="rule rule--one"></div>

    <div class="field-tag field-tag--petals">Petals:</div>
    <div class="rule rule--two"></div>

    <div class="field-tag field-tag--batch">Batch:</div>

    <div class="flower-art" role="img" aria-label="Pale green botanical illustration of calendula flowers with leaves"></div>

    <footer class="origin">
      <p>Fernley Creek</p>
      <p>Victoria Australia</p>
    </footer>
  </main>
</body>
</html>
```